Tallowick Limited Business Card

We need a business card for a new company based in Essex, United Kingdom. We develop and manufacture educational games. The business card needs to match the company brand and logo and the colour scheme.
My company makes educational board games to be played by the family or used by teachers
The games are tile based number game

Target Market(s)

Parents, teachers, schools and children

Industry/Entity Type

Games

Contact Information for Business Card

Company Name - Tallowick Limited
Director - Damian Prouse
Registered Office - 3 Marsh Court, 142 Quarry Lane, Brindleford, Essex, CM7 4XR
Phone Number - 07950 000 318
Email - Enquiries@Tallowick.example
Website - www.Tallowick.example
Company Number - 00000000

Font styles to use
Sans Serif

Colors
00a990
ffffff

Requirements
Must have
• Same colour scheme as the attachments - green and white
• Same font style for Tallowick
• Images of the number tiles similar to the attachments
• extra details
• The colour is Cyan - 82 Magenta - 24 Yellow - 44 Black - 2
• I have attached some of the font styles use on my website and alos my LOGO
Nice to have
• Image of the number "1" tag as seen on the website

```html
<!DOCTYPE html>
<html lang="en">
<head>
<meta charset="utf-8">
<title>Tallowick Limited Business Card</title>
<link rel="stylesheet" href="https://fonts.googleapis.com/css2?family=Lato:wght@400;700;900&display=swap">
<style>
  :root {
    --backdrop: #3a3431;
    --card: #0d0d0d;
    --card-edge: #1c1c1c;
    --brand-teal: #139c9c;
    --text-white: #f2f2f2;
    --text-silver: #cfd2d4;
    --divider: #4a4a4a;
  }
  * { box-sizing: border-box; margin: 0; padding: 0; }
  html, body {
    width: 1200px; height: 900px; overflow: hidden;
    background: var(--backdrop);
    font-family: "Lato", Arial, sans-serif;
  }
  .stage {
    width: 1200px; height: 900px;
    display: flex; align-items: center; justify-content: center; gap: 40px;
  }
  .card {
    width: 540px; height: 310px;
    background: var(--card);
    border: 1px solid var(--card-edge);
    border-radius: 3px;
    position: relative;
    box-shadow: 0 18px 40px rgba(0,0,0,.45);
  }

  /* Contact side */
  .card--contact .brand {
    position: absolute; left: 34px; top: 176px;
  }
  .brand-name {
    font-weight: 900; font-size: 50px; line-height: 1;
    color: var(--brand-teal); letter-spacing: -0.5px;
  }
  .divider {
    position: absolute; left: 282px; top: 48px; width: 1px; height: 210px;
    background: var(--divider);
  }
  .details {
    position: absolute; left: 302px; top: 50px; right: 18px;
    color: var(--text-white); font-size: 14.5px; line-height: 1.45;
  }
  .person-name {
    color: var(--brand-teal); font-weight: 700; font-size: 17px;
    text-transform: uppercase; letter-spacing: 0.3px; line-height: 1.2;
  }
  .person-role { font-size: 13.5px; margin-bottom: 2px; }
  .contact-line { display: flex; align-items: center; gap: 6px; white-space: nowrap; }
  .contact-line svg { width: 11px; height: 11px; fill: var(--brand-teal); flex: none; }
  .address { margin-top: 4px; }
  .company-number { margin-top: 12px; }
  .company-number .label { color: var(--brand-teal); }

  /* Logo side */
  .card--logo { display: flex; align-items: center; justify-content: center; }
  .card--logo .brand-name { color: var(--text-silver); font-size: 54px; }
</style>
</head>
<body>
<main class="stage">
  <section class="card card--contact" aria-label="Business card contact side">
    <div class="brand">
      <div class="brand-name">Tallowick</div>
    </div>
    <div class="divider"></div>
    <div class="details">
      <div class="person-name">Damian Prouse</div>
      <div class="person-role">Director</div>
      <div class="contact-line">
        <svg viewBox="0 0 24 24" aria-hidden="true"><path d="M6.6 10.8a15.1 15.1 0 0 0 6.6 6.6l2.2-2.2c.3-.3.7-.4 1-.2 1.1.4 2.3.6 3.6.6.6 0 1 .4 1 1V20c0 .6-.4 1-1 1C10.6 21 3 13.4 3 4c0-.6.4-1 1-1h3.5c.6 0 1 .4 1 1 0 1.3.2 2.5.6 3.6.1.3 0 .7-.2 1z"/></svg>
        <span>07950 000 318</span>
      </div>
      <div class="contact-line">
        <svg viewBox="0 0 24 24" aria-hidden="true"><path d="M2 5h20v14H2z M2 5l10 8 10-8" stroke="#0d0d0d" stroke-width="1.6"/></svg>
        <span>Enquiries@Tallowick.example</span>
      </div>
      <div class="contact-line">
        <svg viewBox="0 0 24 24" aria-hidden="true"><circle cx="12" cy="12" r="10"/><path d="M2 12h20M12 2c3 3 3 17 0 20M12 2c-3 3-3 17 0 20" stroke="#0d0d0d" stroke-width="1.4" fill="none"/></svg>
        <span>www.Tallowick.example</span>
      </div>
      <div class="address">3 Marsh Court, 142 Quarry Lane<br>Brindleford, Essex, CM7 4XR</div>
      <div class="company-number"><span class="label">Lic Number:</span> 00000000</div>
    </div>
  </section>

  <section class="card card--logo" aria-label="Business card logo side">
    <div class="brand">
      <div class="brand-name">Tallowick</div>
    </div>
  </section>
</main>
</body>
</html>
```